National Virtual accounting firm needs website designed

I need a wordpress website design for a national virtual accounting firm. I will upload my business card, logo, and postcards that I have had designed and followed the same style. I want a similar style to be followed so I can keep the running theme similar.

Services include:

Tax Services:
Tax preparation and planning services for Individuals, businesses, estates, and nonprofits
Full Service Payroll for Businesses
ODV Audit Representation

Consulting:
Entity Selection & Restructuring
Financial Projections & Forecasts
Retirement Planning
IPO Readiness

Accounting:
Bookkeeping
Reviews and Compilations
Payroll Services

Other Services:
CFO Services
Compliance Services
Controller Services
Software Implementations for Brimlane, Corvanta, and Plivorn.

Target Market(s)

small to medium size businesses, and individuals

Industry/Entity Type

accounting firms

Font styles to use
Sans Serif

Colors
59FF00
82FF00
B8FF75
E3FFCB
F4FFEA

Requirements
Must have
• Color schematics from the logo and post cards/business cards

```html
<!DOCTYPE html>
<html lang="en">
<head>
<meta charset="utf-8">
<title>Verdano — Virtual Accounting</title>
<link rel="stylesheet" href="https://fonts.googleapis.com/css2?family=Roboto+Condensed:wght@400;700&family=Roboto:wght@400;500;700&family=Montserrat:wght@400;600;700&display=swap">
<style>
:root{
  --green:#5ab544;
  --green-soft:#cfe9c4;
  --ink:#1d1d1b;
  --text:#55554f;
  --muted:#8a8a84;
  --cream:#f7f6f2;
  --white:#ffffff;
  --dark:#262626;
  --footer:#5f5e5a;
  --faq:#f1f2f4;
  --stage:#000000;
  --photo-a:#8aa3b8;
  --photo-b:#d9dfe4;
}
*{margin:0;padding:0;box-sizing:border-box}
html,body{width:1200px;height:2650px;overflow:hidden;background:var(--stage)}
body{position:relative;font-family:"Roboto",sans-serif;color:var(--text)}
.a{position:absolute}
.panel{position:absolute;overflow:hidden;background:var(--cream)}
.desktop{left:15px;top:21px;width:906px;height:2611px}
.mobile{left:944px;top:21px;width:240px;height:2311px;font-family:"Montserrat",sans-serif}
.band{position:absolute;left:0;width:100%}
.band--white{background:var(--white)}
.band--dark{background:var(--dark)}
.band--footer{background:var(--footer)}
.photo{background:linear-gradient(135deg,var(--photo-a),var(--photo-b));}
.photo--warm{background:linear-gradient(135deg,#c9a46a,#2f3e55)}
.pattern{background:#e2ecd9;opacity:.8}
.brand{font-family:"Roboto",sans-serif;font-weight:500;color:var(--ink);letter-spacing:.5px;display:flex;align-items:center;gap:6px}
.brand__mark{width:14px;height:14px;border-radius:50%;background:var(--green)}
.nav-link{font-size:10px;color:var(--text)}
.nav-link--active{color:var(--green)}
.btn{background:var(--green);color:var(--white);font-weight:500;display:flex;align-items:center;justify-content:center;border-radius:2px}
.eyebrow{font-size:8px;color:var(--muted);letter-spacing:.6px;display:flex;align-items:center;gap:12px}
.eyebrow__dot{width:8px;height:8px;border-radius:50%;background:var(--green)}
.eyebrow--green{color:var(--green);font-weight:700;letter-spacing:1.2px}
.h-cond{font-family:"Roboto Condensed",sans-serif;font-weight:700;color:var(--ink)}
.stat{font-family:"Roboto",sans-serif;font-weight:500;color:var(--ink)}
.stars{color:var(--green);letter-spacing:2px}
.small-bold{font-weight:500;color:var(--ink)}
.body-copy{color:var(--text)}
.body-copy b{color:var(--ink);font-weight:700}
.divider{height:1px;background:var(--green-soft)}
.divider-label{background:var(--cream);color:var(--muted);padding:0 6px}
.check{display:flex;align-items:center;gap:6px;color:var(--text)}
.check__icon{width:8px;height:8px;border:1px solid var(--green);border-radius:50%;position:relative;flex:none}
.check__icon::after{content:"";position:absolute;left:2px;top:2px;width:2px;height:2px;border-radius:50%;background:var(--green)}
.quote-rule{width:2px;background:#777}
.quote-mark{font-family:"Roboto Condensed",sans-serif;font-weight:700;color:var(--green)}
.quote-text{color:var(--white);font-family:"Roboto Condensed",sans-serif;font-weight:700}
.faq-box{background:var(--faq)}
.faq-q{font-weight:700;color:var(--ink);display:flex;justify-content:space-between;gap:10px}
.caret-down{width:0;height:0;border-left:3px solid transparent;border-right:3px solid transparent;border-top:4px solid var(--ink);flex:none;margin-top:3px}
.caret-down--blue{border-top-color:#3aa0d8}
.caret-right{width:0;height:0;border-top:3px solid transparent;border-bottom:3px solid transparent;border-left:4px solid var(--ink);flex:none;margin-top:2px}
.faq-a{color:var(--text)}
.social{display:flex;gap:16px}
.social__icon{width:9px;height:9px;background:#2b2b2b;border-radius:2px}
.social__icon--round{border-radius:50%}
.white-rule{background:var(--white);height:2px}
.footer-nav{color:#d0cfca}
</style>
</head>
<body>

<!-- ============ DESKTOP ============ -->
<main class="panel desktop">
  <header class="band band--white" style="top:0;height:49px">
    <div class="a brand" style="left:103px;top:14px;font-size:16px"><span class="brand__mark"></span>VERDANO</div>
    <nav>
      <span class="a nav-link nav-link--active" style="left:512px;top:18px">Home</span>
      <span class="a nav-link" style="left:557px;top:18px">Our Services</span>
      <span class="a nav-link" style="left:629px;top:18px">About</span>
      <span class="a nav-link" style="left:673px;top:18px">Contact</span>
    </nav>
    <a class="a btn" style="left:726px;top:10px;width:81px;height:27px;font-size:9px">Get Started</a>
  </header>

  <section class="hero">
    <div class="a eyebrow" style="left:117px;top:123px"><span class="eyebrow__dot"></span>LOREM IPSUM IS SIMPLY</div>
    <h1 class="a h-cond" style="left:117px;top:152px;font-size:45px;line-height:53px;width:360px">Lorem Ipsum is simply dummy text of the printing</h1>
    <p class="a body-copy" style="left:117px;top:330px;width:310px;font-size:11.5px;line-height:15.5px"><b>Lorem Ipsum</b> is simply dummy text of the printing and typesetting industry. Lorem Ipsum has been the industry's standard dummy text ever since</p>
    <div class="a pattern" style="left:59px;top:372px;width:117px;height:56px" role="img" aria-label="Green dot grid decoration"></div>
    <a class="a btn" style="left:117px;top:412px;width:84px;height:25px;font-size:8.5px">READ MORE</a>
    <div class="a photo" style="left:512px;top:109px;width:277px;height:414px" role="img" aria-label="Photo of hands using a calculator over financial charts"></div>
  </section>

  <section class="proof">
    <div class="a stat" style="left:117px;top:648px;font-size:40px">4.8</div>
    <div class="a stars" style="left:117px;top:695px;font-size:8px">★★★★★</div>
    <div class="a small-bold" style="left:117px;top:712px;font-size:9px">2,394 Ratings</div>
    <div class="a small-bold" style="left:117px;top:731px;font-size:9px">Ledgerly Reviews</div>
    <div class="a stat" style="left:285px;top:648px;font-size:40px">A+</div>
    <div class="a stars" style="left:285px;top:695px;font-size:8px">★★★★★</div>
    <div class="a small-bold" style="left:285px;top:712px;font-size:9px">Lorem Ipsum is simply</div>
    <div class="a small-bold" style="left:285px;top:731px;font-size:9px">TrustMark Rating</div>
    <h2 class="a h-cond" style="left:451px;top:653px;width:330px;font-size:20px;line-height:26px">Lorem Ipsum is simply dummy text of the printing and typesetting industry.</h2>
    <div class="a h-cond" style="left:451px;top:739px;font-size:11px;color:var(--green)">Lorem Ipsum</div>
    <p class="a body-copy" style="left:451px;top:766px;width:195px;font-size:9.5px;line-height:15px"><b>Lorem Ipsum</b> is simply dummy text of the printing and typesetting industry. Lorem Ipsum has been the industry's standard dummy text ever since</p>
    <div class="a photo" style="left:675px;top:736px;width:66px;height:43px" role="img" aria-label="Photo of a businessman in an office"></div>
  </section>

  <section class="services">
    <div class="a eyebrow eyebrow--green" style="left:117px;top:958px">LOREM IPSUM IS</div>
    <h2 class="a h-cond" style="left:117px;top:985px;width:380px;font-size:29px;line-height:39px">Lorem Ipsum is simply dummy text of the printing</h2>
    <a class="a btn" style="left:685px;top:959px;width:104px;height:25px;font-size:8.5px">View All Services</a>

    <div class="a photo" style="left:117px;top:1090px;width:212px;height:142px" role="img" aria-label="Photo of a tablet showing tax charts"></div>
    <h3 class="a h-cond" style="left:117px;top:1250px;font-size:19px">Tax Services</h3>
    <p class="a body-copy" style="left:117px;top:1287px;width:212px;font-size:9.5px;line-height:15px">Lorem Ipsum is simply dummy text of the printing and typesetting industry. Lorem Ipsum has been the industry's standard dummy text ever since</p>

    <div class="a photo" style="left:347px;top:1090px;width:212px;height:142px" role="img" aria-label="Photo of a consulting meeting in a lounge"></div>
    <h3 class="a h-cond" style="left:347px;top:1250px;font-size:19px">Consulting</h3>
    <p class="a body-copy" style="left:347px;top:1287px;width:212px;font-size:9.5px;line-height:15px">Lorem Ipsum is simply dummy text of the printing and typesetting industry. Lorem Ipsum has been the industry's standard dummy text ever since</p>

    <div class="a photo" style="left:577px;top:1090px;width:212px;height:142px" role="img" aria-label="Photo of accounting documents and a calculator"></div>
    <h3 class="a h-cond" style="left:577px;top:1250px;font-size:19px">Accounting</h3>
    <p class="a body-copy" style="left:577px;top:1287px;width:212px;font-size:9.5px;line-height:15px">Lorem Ipsum is simply dummy text of the printing and typesetting industry. Lorem Ipsum has been the industry's standard dummy text ever since</p>

    <div class="a divider" style="left:117px;top:1383px;width:672px"></div>
    <span class="a divider-label" style="left:418px;top:1377px;font-size:8.5px">Other Services</span>

    <h3 class="a h-cond" style="left:117px;top:1448px;font-size:19px">Tax preparation</h3>
    <ul class="a" style="left:117px;top:1492px;list-style:none;font-size:9px;line-height:22px">
      <li class="check"><span class="check__icon"></span>Tax preparation and planning services</li>
      <li class="check"><span class="check__icon"></span>businesses</li>
      <li class="check"><span class="check__icon"></span>estates</li>
      <li class="check"><span class="check__icon"></span>ODV Audit Representation</li>
      <li class="check"><span class="check__icon"></span>Retirement Planning</li>
    </ul>
    <h3 class="a h-cond" style="left:341px;top:1448px;font-size:19px">CFO Services</h3>
    <ul class="a" style="left:341px;top:1492px;list-style:none;font-size:9px;line-height:22px">
      <li class="check"><span class="check__icon"></span>Entity Selection &amp; Restructuring</li>
      <li class="check"><span class="check__icon"></span>Financial Projections &amp; Forecasts</li>
      <li class="check"><span class="check__icon"></span>Achieve Peace of Mind</li>
      <li class="check"><span class="check__icon"></span>Look Young &amp; Beautiful</li>
      <li class="check"><span class="check__icon"></span>Achieve more in Life</li>
    </ul>
    <div class="a photo photo--warm" style="left:555px;top:1447px;width:232px;height:131px" role="img" aria-label="Photo of a hand over a glowing finance graphic"></div>
  </section>

  <section class="band band--dark" style="top:1657px;height:225px">
    <div class="a quote-rule" style="left:247px;top:47px;height:131px"></div>
    <div class="a quote-mark" style="left:266px;top:40px;font-size:34px">“</div>
    <p class="a quote-text" style="left:266px;top:85px;width:400px;font-size:10.5px;line-height:16px">Lorem Ipsum is simply dummy text of the printing and typesetting industryLorem Ipsum is simply dummy text of the printing and typesetting industry</p>
    <div class="a" style="left:266px;top:135px;width:16px;height:1px;background:var(--green)"></div>
    <div class="a quote-text" style="left:266px;top:146px;font-size:10px">Dana Whitfield</div>
    <div class="a" style="left:266px;top:163px;font-size:9px;color:#bbb">Fashion Model</div>
  </section>

  <section class="band band--white" style="top:1882px;height:395px">
    <h2 class="a h-cond" style="left:0;width:100%;top:56px;text-align:center;font-size:29px">Frequently Asked Questions</h2>
    <div class="a faq-box" style="left:129px;top:132px;width:311px;height:191px">
      <div class="a faq-q" style="left:18px;top:18px;width:278px;font-size:8.5px;line-height:9px">Lorem Ipsum is simply dummy text of the printing and typesetting industry<span class="caret-down"></span></div>
      <p class="a faq-a" style="left:18px;top:48px;width:270px;font-size:9px;line-height:15px">Lorem ipsum dolor sit amet, consectetur adipiscing elit, sed do eiusmod tempor incididunt ut labore et dolore magna aliqua. Ut enim ad minim veniam, quis nostrud exercitation.</p>
      <div class="a faq-q" style="left:18px;top:116px;width:278px;font-size:8.5px;line-height:9px">Lorem Ipsum is simply dummy text of the printing and typesetting industry<span class="caret-right"></span></div>
      <div class="a faq-q" style="left:18px;top:155px;width:278px;font-size:8.5px;line-height:9px">Lorem Ipsum is simply dummy text of the printing and typesetting industry<span class="caret-right"></span></div>
    </div>
    <div class="a faq-box" style="left:464px;top:132px;width:314px;height:191px">
      <div class="a faq-q" style="left:18px;top:18px;width:280px;font-size:8.5px;line-height:9px">Lorem Ipsum is simply dummy text of the printing and typesetting industry<span class="caret-down caret-down--blue"></span></div>
      <p class="a faq-a" style="left:18px;top:48px;width:270px;font-size:9px;line-height:15px">Lorem ipsum dolor sit amet, consectetur adipiscing elit, sed do eiusmod tempor incididunt ut labore et dolore magna aliqua. Ut enim ad minim veniam, quis nostrud exercitation.</p>
      <div class="a faq-q" style="left:18px;top:116px;width:280px;font-size:8.5px;line-height:9px">Lorem Ipsum is simply dummy text of the printing and typesetting industrynar?<span class="caret-right"></span></div>
      <div class="a faq-q" style="left:18px;top:155px;width:280px;font-size:8.5px;line-height:9px">Lorem Ipsum is simply dummy text of the printing and typesetting industry<span class="caret-right"></span></div>
    </div>
  </section>

  <section class="band band--dark" style="top:2277px;height:188px">
    <div class="a white-rule" style="left:117px;top:45px;width:29px"></div>
    <h2 class="a h-cond" style="left:117px;top:59px;font-size:29px;color:var(--white)">Lorem Ipsum is simply dummy text</h2>
    <p class="a" style="left:117px;top:115px;width:220px;font-size:9.5px;line-height:15px;color:#c9c9c9"><b style="color:var(--white)">Lorem Ipsum</b> is simply dummy text of the printing and typesetting industry.</p>
    <a class="a btn" style="left:632px;top:80px;width:90px;height:26px;font-size:8.5px">Call To Action</a>
  </section>

  <footer class="band band--footer" style="top:2465px;height:146px">
    <div class="a" style="left:409px;top:20px;width:89px;height:12px;background:var(--white);display:flex;align-items:center;justify-content:center">
      <span class="brand" style="font-size:8px">VERDANO</span>
    </div>
    <nav class="a footer-nav" style="left:0;width:100%;top:62px;text-align:center;font-size:9px;word-spacing:4px">Home&nbsp; Our Services&nbsp; About&nbsp; Contact</nav>
    <div class="a" style="left:0;top:94px;width:100%;height:1px;background:#8a8985"></div>
    <div class="a" style="left:99px;top:110px;font-size:9px;color:#222">Copyright © 2023 verdano</div>
    <div class="a social" style="left:594px;top:112px">
      <span class="social__icon"></span><span class="social__icon"></span><span class="social__icon"></span><span class="social__icon social__icon--round"></span>
    </div>
  </footer>
</main>

<!-- ============ MOBILE ============ -->
<main class="panel mobile">
  <header class="band band--white" style="top:0;height:20px">
    <div class="a brand" style="left:14px;top:5px;font-size:8px;gap:3px"><span class="brand__mark" style="width:7px;height:7px"></span>VERDANO</div>
    <div class="a" style="right:14px;top:7px;width:10px;height:6px;border-top:1px solid #e3b86a;border-bottom:1px solid #e3b86a"></div>
  </header>

  <div class="a eyebrow" style="left:18px;top:42px;font-size:5.5px"><span class="eyebrow__dot" style="width:6px;height:6px"></span>LOREM IPSUM IS SIMPLY</div>
  <h1 class="a" style="left:18px;top:62px;width:180px;font-size:12px;line-height:14px;font-weight:700;color:var(--ink)">Lorem Ipsum is simply dummy text of the printing</h1>
  <p class="a body-copy" style="left:18px;top:113px;width:200px;font-size:6px;line-height:9px"><b>Lorem Ipsum</b> is simply dummy text of the printing and typesetting industry. Lorem Ipsum has been the industry's standard dummy text ever since</p>
  <div class="a pattern" style="left:4px;top:165px;width:84px;height:38px" role="img" aria-label="Green dot grid decoration"></div>
  <a class="a btn" style="left:18px;top:170px;width:84px;height:15px;font-size:6px">READ MORE</a>
  <div class="a photo" style="left:18px;top:206px;width:192px;height:174px" role="img" aria-label="Photo of hands using a calculator over financial charts"></div>

  <div class="a" style="left:18px;top:400px;font-size:17px;font-weight:700;color:var(--ink)">4.8</div>
  <div class="a stars" style="left:18px;top:421px;font-size:5px">★★★★★</div>
  <div class="a small-bold" style="left:18px;top:431px;font-size:5.5px;line-height:11px;font-weight:700">2,394 Ratings<br>Ledgerly Reviews</div>
  <div class="a" style="left:114px;top:400px;font-size:17px;font-weight:700;color:var(--ink)">A+</div>
  <div class="a stars" style="left:114px;top:421px;font-size:5px">★★★★★</div>
  <div class="a small-bold" style="left:114px;top:431px;font-size:5.5px;line-height:11px;font-weight:700">Lorem Ipsum is simply<br>TrustMark Rating</div>

  <h2 class="a" style="left:18px;top:466px;width:200px;font-size:7.5px;line-height:11px;font-weight:700;color:var(--ink)">Lorem Ipsum is simply dummy text of the printing and typesetting industry.</h2>
  <div class="a photo" style="left:18px;top:500px;width:68px;height:26px" role="img" aria-label="Photo of a businessman in an office"></div>
  <div class="a" style="left:18px;top:535px;font-size:6.5px;font-weight:700;color:var(--green)">Lorem Ipsum</div>
  <p class="a body-copy" style="left:18px;top:551px;width:195px;font-size:5.5px;line-height:9px"><b>Lorem Ipsum</b> is simply dummy text of the printing and typesetting industry. Lorem Ipsum has been the industry's standard dummy text ever since</p>

  <div class="a eyebrow eyebrow--green" style="left:18px;top:617px;font-size:5.5px">LOREM IPSUM IS</div>
  <h2 class="a" style="left:18px;top:631px;width:190px;font-size:8.5px;line-height:11px;font-weight:700;color:var(--ink)">Lorem Ipsum is simply dummy text of the printing</h2>
  <a class="a btn" style="left:18px;top:664px;width:104px;height:16px;font-size:5.5px">View All Services</a>

  <div class="a photo" style="left:18px;top:703px;width:192px;height:77px" role="img" aria-label="Photo of a tablet showing tax charts"></div>
  <div class="a" style="left:18px;top:789px;font-size:7px;font-weight:700;color:var(--ink)">Tax Services</div>
  <p class="a body-copy" style="left:18px;top:806px;width:192px;font-size:5.5px;line-height:9px">Lorem ipsum is simply dummy text of the printing and typesetting industry. Lorem ipsum has been the industry's standard dummy text ever since</p>
  <div class="a photo" style="left:18px;top:855px;width:192px;height:77px" role="img" aria-label="Photo of a consulting meeting in a lounge"></div>
  <div class="a" style="left:18px;top:942px;font-size:7px;font-weight:700;color:var(--ink)">Consulting</div>
  <p class="a body-copy" style="left:18px;top:959px;width:192px;font-size:5.5px;line-height:9px">Lorem ipsum is simply dummy text of the printing and typesetting industry. Lorem ipsum has been the industry's standard dummy text ever since</p>
  <div class="a photo" style="left:18px;top:1008px;width:192px;height:77px" role="img" aria-label="Photo of accounting documents and a calculator"></div>
  <div class="a" style="left:18px;top:1095px;font-size:7px;font-weight:700;color:var(--ink)">Accounting</div>
  <p class="a body-copy" style="left:18px;top:1112px;width:192px;font-size:5.5px;line-height:9px">Lorem ipsum is simply dummy text of the printing and typesetting industry. Lorem ipsum has been the industry's standard dummy text ever since</p>

  <div class="a divider" style="left:18px;top:1169px;width:192px"></div>
  <span class="a divider-label" style="left:82px;top:1165px;font-size:5.5px">Other Services</span>

  <div class="a" style="left:18px;top:1199px;font-size:7px;font-weight:700;color:var(--ink)">Tax preparation</div>
  <ul class="a" style="left:18px;top:1218px;list-style:none;font-size:5.5px;line-height:13.4px;font-weight:600">
    <li class="check"><span class="check__icon" style="width:7px;height:7px"></span>Tax preparation and planning services</li>
    <li class="check"><span class="check__icon" style="width:7px;height:7px"></span>businesses</li>
    <li class="check"><span class="check__icon" style="width:7px;height:7px"></span>estates</li>
    <li class="check"><span class="check__icon" style="width:7px;height:7px"></span>ODV Audit Representation</li>
    <li class="check"><span class="check__icon" style="width:7px;height:7px"></span>Retirement Planning</li>
  </ul>
  <div class="a" style="left:18px;top:1304px;font-size:7px;font-weight:700;color:var(--ink)">CFO Services</div>
  <ul class="a" style="left:18px;top:1323px;list-style:none;font-size:5.5px;line-height:13.4px;font-weight:600">
    <li class="check"><span class="check__icon" style="width:7px;height:7px"></span>Entity Selection &amp; Restructuring</li>
    <li class="check"><span class="check__icon" style="width:7px;height:7px"></span>Financial Projections &amp; Forecasts</li>
    <li class="check"><span class="check__icon" style="width:7px;height:7px"></span>Achieve Peace of Mind</li>
    <li class="check"><span class="check__icon" style="width:7px;height:7px"></span>Look Young &amp; Beautiful</li>
    <li class="check"><span class="check__icon" style="width:7px;height:7px"></span>Achieve more in Life</li>
  </ul>
  <div class="a photo photo--warm" style="left:18px;top:1411px;width:192px;height:64px" role="img" aria-label="Photo of a hand over a glowing finance graphic"></div>

  <section class="band band--dark" style="top:1506px;height:164px">
    <div class="a quote-rule" style="left:18px;top:23px;height:112px"></div>
    <div class="a quote-mark" style="left:38px;top:18px;font-size:22px">“</div>
    <p class="a" style="left:38px;top:46px;width:185px;font-size:6.5px;line-height:10.5px;font-weight:700;color:var(--white)">Lorem Ipsum is simply dummy text of the printing and typesetting industryLorem Ipsum is simply dummy text of the printing and typesetting industry</p>
    <div class="a" style="left:38px;top:112px;width:16px;height:1px;background:var(--green)"></div>
    <div class="a" style="left:38px;top:120px;font-size:6.5px;font-weight:700;color:var(--white)">Dana Whitfield</div>
    <div class="a" style="left:38px;top:131px;font-size:5.5px;color:#bbb">Fashion Model</div>
  </section>

  <section class="band band--white" style="top:1670px;height:321px">
    <h2 class="a" style="left:0;width:100%;top:17px;text-align:center;font-size:8.5px;font-weight:700;color:var(--ink)">Frequently Asked Questions</h2>
    <div class="a faq-box" style="left:14px;top:39px;width:217px;height:264px">
      <div class="a faq-q" style="left:8px;top:10px;width:200px;font-size:5px;line-height:6px">Lorem Ipsum is simply dummy text of the printing and typesetting industry<span class="caret-down"></span></div>
      <p class="a faq-a" style="left:10px;top:30px;width:195px;font-size:5px;line-height:8.5px">Lorem ipsum dolor sit amet, consectetur adipiscing elit, sed do eiusmod tempor incididunt ut labore et dolore magna aliqua. Ut enim ad minim veniam, quis nostrud exercitation.</p>
      <div class="a faq-q" style="left:8px;top:87px;width:200px;font-size:5px;line-height:6px">Lorem Ipsum is simply dummy text of the printing and typesetting industry<span class="caret-right"></span></div>
      <div class="a faq-q" style="left:8px;top:113px;width:200px;font-size:5px;line-height:6px">Lorem Ipsum is simply dummy text of the printing and typesetting industry<span class="caret-right"></span></div>
      <div class="a faq-q" style="left:8px;top:138px;width:200px;font-size:5px;line-height:6px">Lorem Ipsum is simply dummy text of the printing and typesetting industry<span class="caret-down caret-down--blue"></span></div>
      <p class="a faq-a" style="left:10px;top:158px;width:195px;font-size:5px;line-height:8.5px">Lorem ipsum dolor sit amet, consectetur adipiscing elit, sed do eiusmod tempor incididunt ut labore et dolore magna aliqua. Ut enim ad minim veniam, quis nostrud exercitation.</p>
      <div class="a faq-q" style="left:8px;top:216px;width:200px;font-size:5px;line-height:6px">Lorem Ipsum is simply dummy text of the printing and typesetting industrynar?<span class="caret-right"></span></div>
      <div class="a faq-q" style="left:8px;top:241px;width:200px;font-size:5px;line-height:6px">Lorem Ipsum is simply dummy text of the printing and typesetting industry<span class="caret-right"></span></div>
    </div>
  </section>

  <section class="band band--dark" style="top:1991px;height:140px">
    <div class="a white-rule" style="left:105px;top:19px;width:30px;height:1px"></div>
    <h2 class="a" style="left:30px;top:31px;width:180px;text-align:center;font-size:8.5px;line-height:11px;font-weight:700;color:var(--white)">Lorem Ipsum is simply dummy text</h2>
    <p class="a" style="left:30px;top:60px;width:180px;text-align:center;font-size:5px;line-height:8.5px;color:#c9c9c9"><b style="color:var(--white)">Lorem Ipsum</b> is simply dummy text of the printing and typesetting industry.</p>
    <a class="a btn" style="left:75px;top:101px;width:90px;height:15px;font-size:5.5px">Call To Action</a>
  </section>

  <footer class="band band--footer" style="top:2131px;height:180px">
    <div class="a" style="left:73px;top:6px;width:93px;height:15px;background:var(--white);display:flex;align-items:center;justify-content:center">
      <span class="brand" style="font-size:8px">VERDANO</span>
    </div>
    <nav class="a footer-nav" style="left:0;width:100%;top:64px;text-align:center;font-size:5.5px;line-height:9px">Home<br>Our Services<br>About<br>Contact</nav>
    <div class="a" style="left:0;top:132px;width:100%;height:1px;background:#8a8985"></div>
    <div class="a" style="left:0;width:100%;top:143px;text-align:center;font-size:5.5px;color:#222">Copyright © 2023 verdano</div>
    <div class="a social" style="left:80px;top:155px;gap:20px">
      <span class="social__icon" style="width:7px;height:7px"></span><span class="social__icon" style="width:7px;height:7px"></span><span class="social__icon" style="width:7px;height:7px"></span><span class="social__icon social__icon--round" style="width:7px;height:7px"></span>
    </div>
  </footer>
</main>

</body>
</html>
```